Technical Communications firm needs an article turned into a white paper

We want to redesign a 3-part blog series into a white paper that we can print for a conference. I've consolidated the three posts into the attached Word document.

We are looking for a light, easy to read design. Good use of graphics to support the message. I've added the graphics we used in the original post.

You can view them at
http://www.quillmarrowgroup.com/blog/are-you-satisfied-with-your-dita-solution/

Target Market(s)

Product managers from High-tech, Finance, and Medical industries.

Industry/Entity Type

Information Technology

Colors

Designer to choose colors to be used in the design.

Requirements
Must have
• Must be modern, light, easy to read and slick design. Try to incorporate the graphics provided, but feel free to add more. Must retain the lists and tables.
• Must align with our website/brand.
• Must be easy to read. So not too busy.
• Please move all footnotes to endnotes. You'll need to rework the numbering.
Nice to have
• Awesome coverpage.
Should not have
• Hokey clipart. Not too heavy or hard to read.

```html
<!DOCTYPE html>
<html lang="en">
<head>
<meta charset="utf-8">
<title>Are You Satisfied With Your DITA Solutions?</title>
<link rel="stylesheet" href="https://fonts.googleapis.com/css2?family=Roboto:wght@500;700&family=Lato:ital,wght@0,400;0,700;1,400&family=Oswald:wght@500&display=swap">
<style>
:root{
  --backdrop:#dcdcdc;
  --paper:#ffffff;
  --ink:#2b2b2b;
  --heading-blue:#1b5aa6;
  --royal:#2520a6;
  --navy:#1c1691;
  --cyan:#05a6d8;
  --pale-blue:#c9dff0;
  --panel-blue:#cde5ee;
  --panel-grey:#f7f8f8;
  --number-blue:#0d4fa0;
  --photo-dark:#485257;
  --photo-light:#6f7a7f;
}
*{margin:0;padding:0;box-sizing:border-box}
html,body{width:1200px;height:1000px;overflow:hidden}
body{background:var(--backdrop);position:relative;font-family:"Lato",sans-serif;color:var(--ink)}
.page{position:absolute;left:294px;top:77px;width:597px;height:846px;background:var(--paper);overflow:hidden}
.masthead{position:absolute;left:0;top:0;width:597px;height:235px}
.title{position:absolute;left:42px;top:54px;font-family:"Roboto",sans-serif;font-weight:700;color:#fff;font-size:26.5px;line-height:33.5px;letter-spacing:.2px}
.byline{position:absolute;left:42px;top:203px;font-style:italic;color:#fff;font-size:11px;line-height:14px}
.column{position:absolute;font-size:11.2px;line-height:13.2px}
.column p{text-indent:20px;margin-bottom:13px}
.col-left{left:42px;top:257px;width:230px}
.col-right{left:315px;top:257px;width:255px}
.section-head{font-family:"Lato",sans-serif;font-weight:700;color:var(--heading-blue);font-size:14px;margin:0 0 17px}
.col-left .section-head{margin-top:14px}
.col-right .section-head{margin-top:0;margin-bottom:15px}
.issue-list{list-style:none;margin:0 0 13px}
.issue-list li{position:relative;padding-left:20px}
.issue-list li::before{content:"";position:absolute;left:1px;top:5px;width:4px;height:4px;border-radius:50%;background:var(--ink)}
.parts{position:absolute;left:323px;top:348px;width:245px}
.part{position:relative;display:block}
.part svg{position:absolute;left:0;top:0}
.part-number{position:absolute;left:-6px;font-family:"Oswald",sans-serif;font-weight:500;color:var(--number-blue);font-size:54px;line-height:1}
.part-text{position:absolute;left:58px;width:178px;font-size:11.2px;line-height:13.2px}
.part-text strong{color:var(--heading-blue);font-weight:700}
.notes{position:absolute;left:42px;top:757px;width:510px;font-size:7.4px;line-height:9.5px;color:#333}
.folio{position:absolute;left:0;top:809px;width:597px;height:37px}
.folio-text{position:absolute;right:45px;top:12px;font-family:"Roboto",sans-serif;font-weight:700;font-size:10px;color:#fff}
</style>
</head>
<body>
<article class="page">
  <header class="masthead">
    <svg width="597" height="235" viewBox="0 0 597 235">
      <defs>
        <linearGradient id="photoTone" x1="0" y1="0" x2="1" y2="1">
          <stop offset="0" stop-color="var(--photo-dark)"/>
          <stop offset="1" stop-color="var(--photo-light)"/>
        </linearGradient>
      </defs>
      <rect role="img" aria-label="Chalkboard photo with a hand-drawn star rating checklist and a bearded man looking up thoughtfully" x="0" y="0" width="597" height="196" fill="url(#photoTone)"/>
      <polygon points="0,0 60,0 313,196 0,196" fill="var(--royal)"/>
      <polygon points="0,196 313,196 296,235 0,235" fill="var(--navy)"/>
      <polygon points="296,235 318,205 597,198 597,210 330,214 312,235" fill="var(--cyan)"/>
      <polygon points="312,235 330,214 597,210 597,235" fill="var(--pale-blue)"/>
    </svg>
    <h1 class="title">ARE YOU<br>SATISFIED<br>WITH YOUR<br>DITA SOLUTIONS?</h1>
    <p class="byline">By Dale Fenwick – President of Quill Marrow<br>Group Inc.</p>
  </header>

  <section class="column col-left">
    <p>If your answer is “No” then you are not alone according to a 2017 survey of more than 250 technical communication professionals conducted by The Content Drover. The DITA Satisfaction Survey<span style="color:var(--heading-blue)">[i]</span> indicates that 62% of respondents using DITA are—to varying degrees—dissatisfied. As many as 10% of that group were very dissatisfied reporting that their DITA implementation is experiencing ‘big’ challenges. It’s not surprising that there’s significant dissatisfaction amongst those who have adopted DITA. After all, moving to DITA is a seismic shift in technical writing; a big change with many opportunities for things to go wrong.</p>
    <p>The good news is that most DITA users don’t see their problems as insurmountable. Many just need a little help getting to where they’d like to be.</p>
    <h2 class="section-head">Breakdown of the issues</h2>
    <p>The Content Drover DITA Satisfaction Survey asked respondents to rank the top 10 issues facing DITA users. These issues fit into three major categories including</p>
    <ul class="issue-list">
      <li>skills development</li>
      <li>technology, and</li>
      <li>management.</li>
    </ul>
    <p>The DITA Satisfaction Survey Aggregate Results revealed little spread between the ranking of the issues indicating that respondents likely faced more than one issue of concern.</p>
  </section>

  <section class="column col-right">
    <h2 class="section-head">In this article</h2>
    <p>In this article, we examine three issues impacting DITA satisfaction to help you find the best place to start making improvements.</p>
  </section>

  <div class="parts">
    <div class="part" style="height:113px">
      <svg width="245" height="113"><polygon points="0,0 245,0 245,113 0,113 52,56" fill="var(--panel-blue)"/></svg>
      <span class="part-number" style="top:27px">1</span>
      <p class="part-text" style="top:10px"><strong>Part 1: Skills Development</strong> – This problem area is far and away the most pressing obstacle for a successful DITA deployment. Too often authors are left to figure out how to adapt to writing for DITA on their own.</p>
    </div>
    <div class="part" style="height:122px">
      <svg width="245" height="122"><polygon points="0,0 245,0 245,122 0,122 52,61" fill="var(--panel-grey)"/></svg>
      <span class="part-number" style="top:35px">2</span>
      <p class="part-text" style="top:11px"><strong>Part 2: Technology</strong> – We often hear about the failure of the technology as it relates to performance or complexity. While technology may seem the most likely culprit, it is often not the root cause of the problem.</p>
    </div>
    <div class="part" style="height:157px">
      <svg width="245" height="157"><polygon points="0,0 245,0 245,157 0,157 52,78" fill="var(--panel-blue)"/></svg>
      <span class="part-number" style="top:46px">3</span>
      <p class="part-text" style="top:12px"><strong>Part 3: Management</strong> – While these issues appear to be of least concern to many survey respondents, they are most likely to form the root cause of all other issues identified in the survey. This points to a general lack of awareness as to the role management should be playing in collaborative, structured authoring solutions.</p>
    </div>
  </div>

  <footer class="notes">
    <p>FOOT NOTES (Intro)</p>
    <p>[i] DITA Satisfaction Survey published by The Content Drover on May 31, 2017. Listen to an analysis of the results by Dale Fenwick, Keith Amberly-Norton, Mark Lowry, and Scott Rivers and download a copy of the results today from BrightHall at https://www.brighthall.com/webcast/9273/259775</p>
  </footer>

  <div class="folio">
    <svg width="597" height="37"><polygon points="273,37 305,0 597,0 597,37" fill="var(--cyan)"/></svg>
    <span class="folio-text">Quill Marrow 2017 | PAGE 1</span>
  </div>
</article>
</body>
</html>
```